Business card for a boutique travel agency VELARIEN

we need a business card design - double sided. We would like to have a very elegant, sophisticated but modern design. we are travel consultants and our business focus is Europe, mainly the city of Paris. We would like to receive designs in white and silver, black color but if you are confident that we should pick up a color to make it different and more beautful...go ahead! We are going to give business cards to our clients and business partners. It is important to be perceived as elegant, modern and trustful. Please check jpg references.

Target Market(s)

Velarien primary clients are individuals, couples and affinity groups of high-net-worth who travel for leisure at least once per year. Seeking the ultimate travel experience, the target clients demand the finest quality activities and accommodations accompanied by a superior level of service.

Industry/Entity Type

Travel Industry

Contact Information for Business Card

Lucinda Farrow
- lucinda@velarien-example.com
- +55 11 98347.2516
- velarien-example.com
- unique travel experiences (we would like to see this signature printed as a detail)

Font styles to use
Sans Serif

Colors

Designer to choose colors to be used in the design.

Requirements
Must have
• the Velarien logo that I have attached
Nice to have
• we would like to have some nice detail, something different that shows that we care about,... we are detail oriented.
Should not have
• decorative fonts

```html
<!DOCTYPE html>
<html lang="en">
<head>
<meta charset="utf-8">
<title>Velarien — Business Card</title>
<link rel="stylesheet" href="https://fonts.googleapis.com/css2?family=Josefin+Sans:wght@300&family=Open+Sans:wght@400&family=Oswald:wght@600&display=swap">
<style>
  :root {
    --backdrop: #e9e7e4;
    --card-black: #1b1b1b;
    --card-white: #ffffff;
    --silver: #a9a9a9;
    --tagline-grey: #8c8c8c;
    --ink: #111111;
    --shadow: rgba(0, 0, 0, 0.22);
  }
  * { margin: 0; padding: 0; box-sizing: border-box; }
  html, body {
    width: 1200px;
    height: 1000px;
    overflow: hidden;
    background: var(--backdrop);
  }
  .canvas {
    position: relative;
    width: 1200px;
    height: 1000px;
  }
  .card {
    position: absolute;
    left: 266px;
    width: 666px;
    height: 397px;
    box-shadow: 0 4px 12px var(--shadow);
  }
  .card--front {
    top: 74px;
    background: var(--card-black);
  }
  .card--back {
    top: 534px;
    background: var(--card-white);
  }
  .brand-name {
    position: absolute;
    top: 174px;
    left: 0;
    width: 100%;
    text-align: center;
    font-family: "Josefin Sans", sans-serif;
    font-weight: 300;
    font-size: 42px;
    letter-spacing: 16px;
    padding-left: 16px;
    color: var(--silver);
    line-height: 48px;
  }
  .tagline {
    position: absolute;
    top: 349px;
    left: 0;
    width: 100%;
    text-align: center;
    font-family: "Open Sans", sans-serif;
    font-size: 16px;
    color: var(--tagline-grey);
  }
  .holder-name {
    position: absolute;
    left: 99px;
    top: 175px;
    font-family: "Oswald", sans-serif;
    font-weight: 600;
    font-size: 29px;
    letter-spacing: -0.5px;
    text-transform: uppercase;
    color: var(--ink);
    line-height: 40px;
  }
  .divider {
    position: absolute;
    left: 318px;
    top: 168px;
    width: 2px;
    height: 56px;
    background: var(--ink);
  }
  .contact-list {
    position: absolute;
    left: 342px;
    top: 162px;
    list-style: none;
    font-family: "Open Sans", sans-serif;
    font-size: 16px;
    color: var(--ink);
  }
  .contact-item {
    display: flex;
    align-items: center;
    height: 22.5px;
  }
  .contact-icon {
    width: 14px;
    height: 14px;
    margin-right: 7px;
    flex: none;
  }
</style>
</head>
<body>
<main class="canvas">
  <section class="card card--front" aria-label="Card front">
    <h1 class="brand-name">VELARIEN</h1>
    <p class="tagline">Unique Travel Experiences</p>
  </section>

  <section class="card card--back" aria-label="Card back">
    <h2 class="holder-name">Lucinda Farrow</h2>
    <span class="divider" aria-hidden="true"></span>
    <ul class="contact-list">
      <li class="contact-item">
        <svg class="contact-icon" viewBox="0 0 14 14" aria-hidden="true">
          <path d="M1 5 Q7 1 13 5 L11.5 6.5 L9.5 5.5 L9.5 4.3 Q7 3.5 4.5 4.3 L4.5 5.5 L2.5 6.5 Z" fill="#111"/>
          <path d="M3 7.5 L5 6 L9 6 L11 7.5 L12 12 L2 12 Z" fill="#111"/>
          <circle cx="7" cy="9" r="1.4" fill="#fff"/>
        </svg>
        +55 11 98347.2516
      </li>
      <li class="contact-item">
        <svg class="contact-icon" viewBox="0 0 14 14" aria-hidden="true">
          <rect x="1" y="3" width="12" height="9" fill="#111"/>
          <path d="M1 3 L7 8 L13 3" fill="none" stroke="#fff" stroke-width="1"/>
        </svg>
        lucinda@velarien-example.com
      </li>
      <li class="contact-item">
        <svg class="contact-icon" viewBox="0 0 14 14" aria-hidden="true">
          <circle cx="7" cy="7" r="5.5" fill="none" stroke="#111" stroke-width="1.6"/>
          <path d="M1.5 7 H12.5 M7 1.5 Q3.5 7 7 12.5 M7 1.5 Q10.5 7 7 12.5" fill="none" stroke="#111" stroke-width="1.1"/>
        </svg>
        www.velarien-example.com
      </li>
    </ul>
  </section>
</main>
</body>
</html>
```